This book will apply the 12 Steps to gaming addiction, also known as video game addiction. The primary purpose of the book is to provide an effective solution for this new type of addiction. The solution is based on the rich and successful concepts of traditional twelve-step programs like RL.

The title on the cover will be "Nine Doors Past the Glowing Screen" and "by Martin Quorby". A subtitle can be used if it works in your design of "A Practical Path Beyond Compulsive Console Play". Cover will be for a 6" x 9" book approximately 110 pages in length.

Some back cover text including some review quotes and an author bio are in the attached Word doc. There is also an author photo attached for for the back cover.

Requirements
Must have
• For the cover design it could be stylized, or an image, a partial image, or whatever. I am open to suggestions. Think about what would be noticed by a person searching for help with moderating their video game use, or by the parents or loved ones of problem gamers. Something contemporary and eye catching.

```html
<!DOCTYPE html>
<html lang="en">
<head>
<meta charset="UTF-8">
<title>Nine Doors Past the Glowing Screen — Cover Spread</title>
<link href="https://fonts.googleapis.com/css2?family=Oswald:wght@300;400;600;700&family=Open+Sans:wght@400;600&display=swap" rel="stylesheet">
<style>
  :root {
    --stage: #5a5a5a;
    --paper: #ffffff;
    --ink-grey: #5b5b5b;
    --ink-dark: #3a3a3a;
    --accent: #f08a1c;
    --rule: #9a9a9a;
    --photo-blue: #8fb3cf;
    --photo-warm: #d8b27a;
    --portrait: #b9a48c;
  }
  * { box-sizing: border-box; margin: 0; padding: 0; }
  html, body { width: 800px; height: 1200px; overflow: hidden; }
  body {
    background: var(--stage);
    font-family: "Open Sans", Arial, sans-serif;
    display: flex;
    align-items: center;
    justify-content: center;
  }
  .spread { display: flex; gap: 14px; align-items: stretch; }
  .panel {
    background: var(--paper);
    height: 522px;
    position: relative;
    padding: 10px;
  }
  .panel__frame {
    height: 100%;
    border: 1.5px dashed var(--rule);
    position: relative;
    overflow: hidden;
  }

  /* Front cover */
  .front { width: 348px; }
  .front .panel__frame { display: flex; flex-direction: column; align-items: center; }
  .title { text-align: center; font-family: "Oswald", Arial Narrow, sans-serif; text-transform: uppercase; margin-top: 26px; line-height: 1; }
  .title__lead { font-weight: 300; color: var(--ink-grey); font-size: 28px; letter-spacing: 1px; }
  .title__accent { font-weight: 700; color: var(--accent); font-size: 40px; margin-top: 4px; }
  .title__main { font-weight: 400; color: var(--ink-grey); font-size: 54px; letter-spacing: 1px; margin-top: 2px; }
  .subtitle-bar {
    background: var(--accent); color: var(--paper);
    font-size: 8.5px; font-weight: 600; letter-spacing: .5px; text-transform: uppercase;
    padding: 4px 10px; margin-top: 10px; width: 88%; text-align: center;
  }
  .author { font-family: "Oswald", Arial Narrow, sans-serif; color: var(--ink-grey); font-size: 20px; letter-spacing: 2px; text-transform: uppercase; margin-top: 12px; }
  .cover-photo {
    margin-top: auto; width: 100%; height: 230px;
    background: linear-gradient(180deg, #eef1f3 0%, var(--photo-blue) 55%, var(--photo-warm) 100%);
  }

  /* Spine */
  .spine { width: 62px; }
  .spine .panel__frame { display: flex; flex-direction: column; align-items: center; justify-content: space-between; padding: 16px 0; }
  .spine__title, .spine__author { writing-mode: vertical-rl; font-family: "Oswald", Arial Narrow, sans-serif; text-transform: uppercase; white-space: nowrap; }
  .spine__title { font-size: 17px; color: var(--ink-grey); font-weight: 400; }
  .spine__title b { color: var(--accent); font-weight: 700; }
  .spine__author { font-size: 14px; color: var(--ink-dark); letter-spacing: 2px; }

  /* Back cover */
  .back { width: 348px; }
  .back .panel__frame { padding: 20px 20px 16px; display: flex; flex-direction: column; }
  .praise-heading { font-family: "Oswald", Arial Narrow, sans-serif; color: var(--accent); font-weight: 600; font-size: 15px; text-transform: uppercase; text-align: center; line-height: 1.2; margin-bottom: 14px; }
  .review { font-size: 8.2px; line-height: 1.6; color: var(--ink-dark); margin-bottom: 12px; text-align: justify; }
  .review__source { display: block; font-weight: 600; text-align: right; color: var(--ink-grey); margin-top: 2px; }
  .bio { margin-top: auto; display: flex; gap: 10px; align-items: flex-start; }
  .bio__portrait { flex: 0 0 70px; height: 84px; background: linear-gradient(160deg, #e7e1d8, var(--portrait)); }
  .bio__text { font-size: 8.2px; line-height: 1.6; color: var(--ink-dark); }
  .bio__name { color: var(--accent); font-weight: 600; }
</style>
</head>
<body>
  <main class="spread">
    <section class="panel front">
      <div class="panel__frame">
        <h1 class="title">
          <div class="title__lead">Nine Doors Past</div>
          <div class="title__accent">The Glowing</div>
          <div class="title__main">Screen</div>
        </h1>
        <p class="subtitle-bar">A Practical Path Beyond Compulsive Console Play</p>
        <p class="author">Martin Quorby</p>
        <div class="cover-photo" role="img" aria-label="Photograph of two young boys sitting on a bench, absorbed in handheld game devices"></div>
      </div>
    </section>

    <section class="panel spine">
      <div class="panel__frame">
        <p class="spine__title">Nine Doors Past <b>The Glowing Screen</b></p>
        <p class="spine__author">Martin Quorby</p>
      </div>
    </section>

    <section class="panel back">
      <div class="panel__frame">
        <h2 class="praise-heading">Praise for Nine Doors Past<br>the Glowing Screen</h2>
        <p class="review">A clear and caring guide for every family that has watched a loved one disappear into endless play. Quorby offers steady steps, honest stories and real hope for lasting change at home.<span class="review__source">— Dana Whitfield, family counselor</span></p>
        <p class="review">This book meets gamers where they are. The steps are simple to follow, and each chapter ends with questions that invite reflection rather than shame. A welcome resource for parents and players alike.<span class="review__source">— Rafael Ortun, youth mentor</span></p>
        <p class="review">I finally understood why I could not stop playing. Reading one chapter each night gave me the tools to take my evenings back and reconnect with friends offline.<span class="review__source">— A grateful reader</span></p>
        <div class="bio">
          <div class="bio__portrait" role="img" aria-label="Author portrait photograph"></div>
          <p class="bio__text"><span class="bio__name">Martin Quorby</span> is a recovery coach who has spent many years helping gamers and their families find balance. He writes and speaks about healthy screen habits and leads weekly support groups for young adults.</p>
        </div>
      </div>
    </section>
  </main>
</body>
</html>
```